corporate design for "Alvenhütte" a lodge hotel in one of the most famous parts in Germany.

What we need is a design for our Lodge. We offer 136 Beds in 29 Rooms on the mountain in famous Garmisch-Partenkirchen. Our guests have a straight sight to the top of Zugspitze which is the highest peak of germany. We have some very different business models. 1. Most of the year we host birthday party groups and wedding groups. Usually they come for two days to have great celebrations here with about 60-120 gueste "exclusive". 2. Especially befoe x-mas but also durig the year we have companies here, to hold strategy meetings, or teambuilding events (we want to grow that business especially). 3. during the week we host school classes to get the "hotel" fully booked.
What we need is a coorparate style including logo, website, cards, etc. the whole programm.
The main focus is "wood, mauntains, wilderness, lodge,..."
I will upload some pictures and the logo so far.
What I really like is a theme called KALVEST (www.klvtheme.com) with all its parallax and background style. Our website so far is www.alvenhuette.com.
Budget is not the issue as long as it is really looking amazing.

Industry/Entity Type
Hotel
Logo Text
Alvenhütte Garmisch-Partenkirchen
Number of Pages Required
1 page
Requirements
Must have
- I want to host the page in WIX. It has to be responsive and very modern.

```html
<!DOCTYPE html>
<html lang="de">
<head>
<meta charset="utf-8">
<title>Kalvenkopf- &amp; Alvenhütte</title>
<link href="https://fonts.googleapis.com/css2?family=Cinzel:wght@400;700&family=Caveat:wght@400&family=Open+Sans:wght@400&display=swap" rel="stylesheet">
<style>
:root{
  --gold:#d4a35c;
  --gold-soft:#e6bf86;
  --ink:#2b2b2b;
  --muted:#8a8a8a;
  --white:#ffffff;
  --dark:#0f0f0f;
  --darker:#161616;
  --line:rgba(255,255,255,.55);
}
*{margin:0;padding:0;box-sizing:border-box}
html,body{width:1200px;height:2571px;overflow:hidden;background:var(--white)}
body{position:relative;font-family:"Caveat",cursive;color:var(--ink)}
section,header,footer{position:absolute;left:0;width:1200px}
.abs{position:absolute}
.center{left:0;width:1200px;text-align:center}
.photo{position:absolute;inset:0}

/* hero */
.hero{top:0;height:614px;overflow:hidden}
.hero .photo{background:linear-gradient(100deg,#5a3b2a 0%,#8c6a55 14%,#c9b5a2 28%,#7b5540 40%,#b99b86 52%,#6e4836 62%,#a8826b 74%,#9a3f36 84%,#c8a58c 92%,#4b2f22 100%)}
.hero-shade{position:absolute;inset:0;background:linear-gradient(180deg,rgba(20,12,8,.5) 0%,rgba(20,12,8,.42) 50%,rgba(20,12,8,.55) 100%)}
.topbar{position:absolute;top:0;left:0;width:1200px;height:48px;font-family:"Open Sans",sans-serif;font-size:11px;color:var(--white)}
.contact{position:absolute;top:15px;display:flex;align-items:center;gap:8px}
.contact svg{width:16px;height:16px}
.social{position:absolute;top:8px;right:86px;display:flex;gap:20px}
.social span{width:26px;height:26px;border-radius:50%;background:var(--gold)}
.nav{position:absolute;top:64px;left:91px;display:flex;font-family:"Cinzel",serif;font-size:13px;color:var(--white)}
.nav a{color:inherit;text-decoration:none;margin-right:62px}
.nav a.active{color:var(--gold)}
.search{position:absolute;top:59px;left:1078px;width:32px;height:30px;border:1px solid var(--white)}
.logo{display:flex;justify-content:center;align-items:center;gap:12px}
.logo .mark{width:14px;height:14px;border-radius:50%;background:var(--gold)}
.logo .name{font-family:"Cinzel",serif;font-weight:700;color:var(--white);font-size:30px;letter-spacing:1px}
.hero .logo{top:206px}
.hero-title{top:300px;font-size:44px;color:var(--gold-soft)}
.hero-title .rule{display:inline-block;vertical-align:middle;width:252px;height:1px;background:var(--line);margin:0 22px}
.hero-welcome{top:386px;font-family:"Cinzel",serif;font-weight:700;font-size:28px;color:var(--white)}
.dots{top:544px;display:flex;justify-content:center;gap:10px}
.dots span{width:9px;height:9px;border-radius:50%;background:var(--white)}
.dots span.on{background:var(--gold)}

/* service */
.service{top:614px;height:649px}
.section-title{font-family:"Cinzel",serif;font-weight:700;color:var(--gold);font-size:27px}
.section-title .rule{display:inline-block;vertical-align:middle;width:236px;height:1px;background:#cfcfcf;margin:0 22px}
.service .section-title{top:94px}
.service-sub{top:152px;font-size:26px;color:var(--muted)}
.card{position:absolute;top:248px;width:242px}
.card .img{height:206px}
.card h3{margin-top:26px;font-family:"Cinzel",serif;font-weight:700;font-size:16px;color:var(--gold)}
.card p{margin-top:6px;font-size:15px;line-height:23px;color:var(--ink)}

/* groups */
.groups{top:1263px;height:429px}
.groups .img{position:absolute;left:0;top:0;width:600px;height:429px;background:linear-gradient(172deg,#4f78c0 0%,#9fb6d8 18%,#e9eef5 30%,#a9b4c2 40%,#3b4638 55%,#1e2a1c 68%,#5a5236 82%,#7a4a35 100%)}
.groups h2{position:absolute;left:636px;top:48px;font-family:"Cinzel",serif;font-weight:700;font-size:23px;color:var(--gold)}
.groups .rule{position:absolute;left:636px;top:94px;width:240px;height:1px;background:#cfcfcf}
.groups .lead{position:absolute;left:636px;top:116px;width:420px;font-size:26px;line-height:36px;color:var(--ink)}
.groups .body{position:absolute;left:636px;top:222px;width:470px;font-size:16px;line-height:26px;color:var(--muted)}
.btn{position:absolute;left:636px;top:333px;width:136px;height:43px;border:1px solid var(--gold);border-radius:22px;font-family:"Open Sans",sans-serif;font-size:14px;color:var(--ink);text-align:center;line-height:41px}

/* outdoor */
.outdoor{top:1692px;height:512px;overflow:hidden}
.outdoor .photo{background:linear-gradient(180deg,#1f2838 0%,#3a475a 20%,#5d6a7c 38%,#8b95a3 50%,#56606c 60%,#8e97a3 72%,#d7dce3 86%,#eef0f3 100%)}
.outdoor .shade{position:absolute;inset:0;background:rgba(10,14,22,.35)}
.outdoor .section-title{top:154px;color:var(--white)}
.outdoor .section-title .rule{width:255px;background:var(--line)}
.outdoor-sub{top:214px;font-size:27px;color:var(--gold-soft)}
.outdoor-text{top:290px;font-size:21px;line-height:34px;color:var(--white)}
.arrow{position:absolute;top:234px;width:46px;height:46px;border-radius:50%;background:rgba(0,0,0,.55);border:1px solid rgba(255,255,255,.4)}
.arrow svg{width:44px;height:44px}

/* footer */
.footer{top:2204px;height:302px;background:var(--dark)}
.footer .logo{top:126px}
.footer-nav{top:210px;font-family:"Cinzel",serif;font-size:14px;color:#d9d9d9}
.footer-nav .sep{margin:0 10px;color:#888}
.bottom{top:2506px;left:0;width:1200px;height:65px;background:var(--darker);border-top:1px solid #2a2a2a;font-family:"Open Sans",sans-serif;font-size:13px;color:#cfcfcf;text-align:center;line-height:63px}
</style>
</head>
<body>

<header class="hero">
  <div class="photo" role="img" aria-label="Festlich gedeckte Tafel mit Gläsern, Kerzen und Blumen in der Hüttenstube"></div>
  <div class="hero-shade"></div>
  <div class="topbar">
    <div class="contact" style="left:86px">
      <svg viewBox="0 0 16 16"><circle cx="8" cy="8" r="8" fill="#fff"/><rect x="4" y="5" width="8" height="6" fill="none" stroke="#333"/><path d="M4 5l4 3 4-3" fill="none" stroke="#333"/></svg>
      info@alvenhuette.com
    </div>
    <div class="contact" style="left:243px">
      <svg viewBox="0 0 16 16"><circle cx="8" cy="8" r="8" fill="#fff"/><rect x="5.5" y="3.5" width="5" height="9" rx="1" fill="none" stroke="#333"/></svg>
      08821 4720
    </div>
    <div class="social"><span></span><span></span><span></span></div>
  </div>
  <nav class="nav">
    <a class="active">Home</a><a>Die Hütt'n</a><a>Für Gruppen</a><a>Für Firmen</a><a>Zum Feiern</a><a>Mit vielen Aktivitäten</a>
  </nav>
  <div class="search">
    <svg viewBox="0 0 32 30" width="30" height="28"><circle cx="14" cy="13" r="6" fill="none" stroke="#fff" stroke-width="2"/><path d="M18.5 17.5l5 5" stroke="#fff" stroke-width="2"/></svg>
  </div>
  <div class="abs center logo"><span class="mark"></span><span class="name">Alvenhütte</span></div>
  <div class="abs center hero-title"><span class="rule"></span>Kalvenkopf- &amp; Alvenhütte<span class="rule"></span></div>
  <div class="abs center hero-welcome">Herzlich willkommen auf unseren Seiten!</div>
  <div class="abs center dots"><span></span><span class="on"></span><span></span></div>
</header>

<section class="service">
  <h2 class="abs center section-title"><span class="rule"></span>Service<span class="rule"></span></h2>
  <p class="abs center service-sub">Hier gelangen Sie zu unserer Service Area. Bilder, Anreise, Downloads, Kontakt, etc.</p>
  <article class="card" style="left:86px">
    <div class="img" role="img" aria-label="Holzhütte mit Terrasse, Blumen und Bergblick" style="background:linear-gradient(100deg,#5a3320 0%,#7a4a2e 35%,#9dbbe0 55%,#e8eef6 68%,#6f9a3e 85%,#4f7a2c 100%)"></div>
    <h3>Bilder / Impressionen</h3>
    <p>Eine Sammlung von Bildern die unser Hüttenresort, sowie die umgebende Landschaft und Impressionen zeigt.</p>
  </article>
  <article class="card" style="left:348px">
    <div class="img" role="img" aria-label="Verschneiter Berggipfel im Abendlicht" style="background:linear-gradient(180deg,#7f9aa6 0%,#c9b08a 25%,#e7c89c 42%,#8b6a52 58%,#2f3c48 78%,#1f2a34 100%)"></div>
    <h3>Landkarte / Umgebung</h3>
    <p>Eine interaktive Landkarte zeigt Tourvorschläge, Reiseziele und Aktivitäten in der Umgebung.</p>
  </article>
  <article class="card" style="left:609px">
    <div class="img" role="img" aria-label="Geländewagen vor Bergkulisse und Tannen" style="background:linear-gradient(180deg,#c9ccd0 0%,#8e9396 22%,#3a3f3c 45%,#1e2220 70%,#4a4d4f 100%)"></div>
    <h3>Anreise / Abholservice</h3>
    <p>Die direkte Anfahrt mit dem PKW oder Bus zu uns auf die Hütte ist NICHT möglich! Größere Gruppen können,</p>
  </article>
  <article class="card" style="left:872px">
    <div class="img" role="img" aria-label="Winterliches Bergpanorama unter blauem Himmel" style="background:linear-gradient(180deg,#1b56a6 0%,#5f8fcb 30%,#b9cbe2 48%,#5b6570 62%,#8d96a0 76%,#eef0f3 100%)"></div>
    <h3>Anfrage / Kontakt</h3>
    <p>Mit Hilfe dieses Formulars können wir uns ein genaueres Bild Ihrer Wünsche und Bedürfnisse machen.</p>
  </article>
</section>

<section class="groups">
  <div class="img" role="img" aria-label="Hütte mit Biertischen in der Abendsonne vor Bergwald"></div>
  <h2>Schüler- &amp; Gruppenreisen</h2>
  <div class="rule"></div>
  <p class="lead">Die Kalvenkopf- und Alvenhütte ist idealst geeignet für Klassenfahrten</p>
  <p class="body">Im Winter kommen Schüler- &amp; Jugendgruppen natürlich vor allem zum Ski- &amp; Snowboard fahren zu uns. Durch die direkte Anbindung an die Pisten des Alpen Classic Skigebietes sind bei uns beste Vorraussetzungen geschaffen</p>
  <div class="btn">VIEW ALL</div>
</section>

<section class="outdoor">
  <div class="photo" role="img" aria-label="Wanderer im Schnee über dem Tal mit Bergpanorama"></div>
  <div class="shade"></div>
  <h2 class="abs center section-title"><span class="rule"></span>Outdoor &amp; Adventure<span class="rule"></span></h2>
  <p class="abs center outdoor-sub">Hier finden Sie Aktivitäten, Touren und Ausflugsziele bei uns und in der nächsten Umgebung!</p>
  <p class="abs center outdoor-text">In unmittelbarer Nähe zu unserer Hütte, den Auffahrtsweg von der Gratbahn Talstation<br>zu unskreuzend, befindet sich die historische</p>
  <div class="arrow" style="left:12px"><svg viewBox="0 0 46 46"><path d="M26 15l-8 8 8 8" fill="none" stroke="#fff" stroke-width="2"/></svg></div>
  <div class="arrow" style="left:1116px"><svg viewBox="0 0 46 46"><path d="M20 15l8 8-8 8" fill="none" stroke="#fff" stroke-width="2"/></svg></div>
</section>

<footer class="footer">
  <div class="abs center logo"><span class="mark"></span><span class="name">Alvenhütte</span></div>
  <nav class="abs center footer-nav">
    Home<span class="sep">/</span>Die Hütt'n<span class="sep">/</span>Für Gruppen<span class="sep">/</span>Für Firmen<span class="sep">/</span>Zum Feiern<span class="sep">/</span>Mit vielen Aktivitäten
  </nav>
</footer>
<div class="abs bottom">© Alvenhütte all reserved.com</div>

</body>
</html>
```